Design a Flat design copy of this flyer

Copy the brochure but use flat design instead of 3D.
Copy placement of items.

Winning designer will be awarded website development work for word press site.

```html
<!DOCTYPE html>
<html lang="en">
<head>
<meta charset="utf-8">
<title>BLS – Sky Nest</title>
<link rel="stylesheet" href="https://fonts.googleapis.com/css2?family=Open+Sans:wght@400;600;700&family=Fredoka:wght@600&display=swap">
<style>
  :root {
    --navy: #1f3b5f;
    --navy-ink: #1b2f4c;
    --footer: #3e5478;
    --white: #ffffff;
    --lime: #c6cf48;
    --olive: #a6ab3c;
    --gold: #e6a42d;
    --yellow: #e3c02e;
    --green: #56b247;
    --green-dark: #2f9a4a;
    --green-light: #7cc35d;
    --teal: #4b9b99;
    --orange: #ee6a2c;
    --blue: #2f9bd6;
    --brand: #4a3a8c;
  }
  * { box-sizing: border-box; margin: 0; padding: 0; }
  html, body { width: 1200px; height: 870px; overflow: hidden; }
  body { font-family: "Open Sans", Arial, sans-serif; background: var(--navy); }
  .canvas { position: relative; width: 1200px; height: 870px; background: var(--navy); overflow: hidden; }

  .brand {
    position: absolute; left: 53px; top: 57px; width: 83px; height: 86px;
    background: var(--brand); color: var(--white);
    font-weight: 700; font-size: 30px; display: flex; align-items: center; justify-content: center;
  }

  .tabs { position: absolute; top: 68px; left: 335px; height: 49px; display: flex; }
  .tab {
    height: 49px; display: flex; align-items: center; justify-content: center;
    color: var(--white); font-size: 21px; font-weight: 400;
    clip-path: polygon(4% 0, 100% 0, 96% 100%, 0 100%);
    margin-right: -6px;
  }
  .tab--privacy { width: 160px; background: var(--lime); }
  .tab--security { width: 166px; background: var(--teal); }
  .tab--languages { width: 274px; background: var(--orange); }
  .tab--personal { width: 237px; background: var(--green); }

  .opt-in {
    position: absolute; left: 966px; top: 154px; width: 183px; height: 50px;
    background: var(--green); padding: 5px 9px 5px 76px;
  }
  .opt-in span {
    display: flex; height: 100%; align-items: center; justify-content: center;
    background: var(--white); color: var(--green-dark); font-weight: 700; font-size: 20px;
  }

  .category-grid { position: absolute; top: 198px; display: flex; flex-direction: column; gap: 15px; }
  .category-grid--left { left: 57px; }
  .category-grid--mid { left: 409px; }
  .category { display: flex; height: 53px; gap: 8px; }
  .category__icon {
    width: 71px; height: 53px; background: var(--white);
    display: flex; align-items: center; justify-content: center;
  }
  .category-grid--mid .category__icon { width: 66px; }
  .category__icon svg { width: 34px; height: 34px; fill: var(--navy-ink); }
  .category__label {
    width: 218px; display: flex; align-items: center; justify-content: center;
    font-size: 16px; color: var(--navy-ink);
  }
  .category-grid--mid .category__label { width: 226px; }
  .category__label strong { color: var(--white); font-weight: 700; margin-right: 5px; }
  .c-gold { background: var(--gold); }
  .c-green { background: var(--green-dark); }
  .c-teal { background: var(--teal); }
  .c-lime { background: var(--lime); }
  .c-orange { background: var(--orange); }
  .c-olive { background: var(--olive); }
  .c-yellow { background: var(--yellow); }
  .c-blue { background: var(--blue); }

  .offer-bubble {
    position: absolute; left: 750px; top: 245px; width: 399px; height: 198px;
    background: var(--green); color: var(--white); padding: 40px 0 0 14px;
  }
  .offer-bubble::after {
    content: ""; position: absolute; left: 300px; bottom: -27px;
    border-left: 14px solid transparent; border-right: 22px solid transparent;
    border-top: 28px solid var(--green);
  }
  .offer-bubble__title {
    position: absolute; left: 0; top: 0; width: 185px; height: 33px;
    background: var(--green-light); font-size: 19px; font-weight: 600;
    padding: 3px 0 0 10px;
  }
  .bullet-list { list-style: none; }
  .bullet-list li { font-size: 16.5px; line-height: 29px; display: flex; align-items: center; }
  .bullet-list li::before {
    content: ""; width: 10px; height: 12px; border: 1.5px solid var(--white);
    margin-right: 9px; flex-shrink: 0;
  }

  .needs-bubble {
    position: absolute; left: 260px; top: 560px; width: 441px; height: 169px;
    background: var(--orange); color: var(--white); padding: 8px 0 0 16px;
  }
  .needs-bubble::after {
    content: ""; position: absolute; right: -24px; top: 36px;
    border-top: 12px solid transparent; border-bottom: 12px solid transparent;
    border-left: 25px solid var(--orange);
  }

  .figure { position: absolute; }
  .figure--orange {
    left: 716px; top: 452px; width: 170px; height: 292px;
    background: linear-gradient(180deg, #f07a3a, #e0591f);
    border-radius: 80px 80px 20px 20px;
  }
  .figure--green {
    left: 1008px; top: 486px; width: 104px; height: 258px;
    background: linear-gradient(180deg, #6cc04c, #4aa63e);
    border-radius: 52px 52px 14px 14px;
  }
  .product-name {
    position: absolute; left: 829px; top: 590px; width: 273px;
    font-family: "Fredoka", "Arial Rounded MT Bold", sans-serif; font-weight: 600;
    color: var(--white); font-size: 58px; line-height: 62px;
  }
  .product-name span { display: block; }
  .product-name span + span { padding-left: 110px; }

  .sharing {
    position: absolute; left: 40px; top: 565px; width: 146px; text-align: center; color: var(--white);
  }
  .sharing__art {
    width: 132px; height: 136px; margin: 0 auto; border-radius: 50%;
    background: conic-gradient(#2f9bd6, #56b247, #e3c02e, #ee6a2c, #d8342c, #4a3a8c, #2f9bd6);
  }
  .sharing__label { font-size: 14px; margin-top: 8px; }

  .footer {
    position: absolute; left: 0; top: 768px; width: 1200px; height: 102px;
    background: var(--footer); color: var(--white); text-align: center;
    padding-top: 16px; font-size: 19px; line-height: 31px;
  }
</style>
</head>
<body>
<main class="canvas">
  <div class="brand">BLS</div>

  <nav class="tabs">
    <div class="tab tab--privacy">Privacy</div>
    <div class="tab tab--security">Security</div>
    <div class="tab tab--languages">Multiple Languages</div>
    <div class="tab tab--personal">Personalisation</div>
  </nav>

  <div class="opt-in"><span>Opt In</span></div>

  <section class="category-grid category-grid--left">
    <div class="category">
      <div class="category__icon"><svg viewBox="0 0 32 32"><circle cx="11" cy="10" r="5"/><circle cx="22" cy="10" r="5"/><path d="M2 26c0-6 4-9 9-9s9 3 9 9h-3c0-4-3-6-6-6s-6 2-6 6z"/><path d="M21 17c5 0 9 3 9 9h-3c0-4-3-6-6-6z"/></svg></div>
      <div class="category__label c-gold">Friends, Family, Contacts</div>
    </div>
    <div class="category">
      <div class="category__icon"><svg viewBox="0 0 32 32"><path d="M16 3 2 16h4v13h8v-8h4v8h8V16h4z"/></svg></div>
      <div class="category__label c-green">Properties</div>
    </div>
    <div class="category">
      <div class="category__icon"><svg viewBox="0 0 32 32"><path d="M13 5 1 16h3v12h7v-7h4v7h7V16h3z"/><rect x="22" y="14" width="9" height="14"/></svg></div>
      <div class="category__label c-teal">Utilities</div>
    </div>
    <div class="category">
      <div class="category__icon"><svg viewBox="0 0 32 32"><path d="M16 3C8 3 2 9 2 16h28C30 9 24 3 16 3z"/><path d="M15 16h2v10a4 4 0 0 1-8 0h2a2 2 0 0 0 4 0z"/></svg></div>
      <div class="category__label c-lime">Insurances</div>
    </div>
    <div class="category">
      <div class="category__icon"><svg viewBox="0 0 32 32"><path d="M7 7h18l3 9v10h-4v-3H8v3H4V16zm2 3-2 6h18l-2-6z"/><circle cx="9" cy="19" r="1.6" fill="#fff"/><circle cx="23" cy="19" r="1.6" fill="#fff"/></svg></div>
      <div class="category__label c-orange">Vehicles</div>
    </div>
  </section>

  <section class="category-grid category-grid--mid">
    <div class="category">
      <div class="category__icon"><svg viewBox="0 0 32 32"><rect x="3" y="9" width="22" height="13" rx="1" transform="rotate(-12 14 15)"/><rect x="8" y="14" width="22" height="13" rx="1"/><circle cx="19" cy="20.5" r="3" fill="#fff"/></svg></div>
      <div class="category__label c-olive">Financial</div>
    </div>
    <div class="category">
      <div class="category__icon"><svg viewBox="0 0 32 32"><path d="M28 4c-2-1-4 0-6 2l-4 4-12-3-2 2 9 6-4 4-4-1-2 2 5 3 3 5 2-2-1-4 4-4 6 9 2-2-3-12 4-4c2-2 3-4 2-6z"/></svg></div>
      <div class="category__label c-yellow">Travel</div>
    </div>
    <div class="category">
      <div class="category__icon"><svg viewBox="0 0 32 32"><path d="M16 28 4 16a7 7 0 0 1 12-9 7 7 0 0 1 12 9z"/><path d="M7 16h5l2-4 3 7 2-3h6" stroke="#fff" stroke-width="1.8" fill="none"/></svg></div>
      <div class="category__label c-teal">Biometrics</div>
    </div>
    <div class="category">
      <div class="category__icon"><svg viewBox="0 0 32 32"><path d="M16 6c8 0 13 4 13 9s-5 9-13 9c-2 0-3 0-5-1l-6 3 2-5c-2-2-4-4-4-6 0-5 5-9 13-9z"/></svg></div>
      <div class="category__label c-orange">Notifications</div>
    </div>
    <div class="category">
      <div class="category__icon"><svg viewBox="0 0 32 32"><rect x="12" y="11" width="10" height="10" rx="2"/><path d="M22 13h6v2h-6zm0 4h6v2h-6zM4 15h8v2H4z"/></svg></div>
      <div class="category__label c-blue"><strong>API</strong> Designer / Plugin</div>
    </div>
  </section>

  <section class="offer-bubble">
    <h2 class="offer-bubble__title">Offering users:</h2>
    <ul class="bullet-list">
      <li>Transparent Opt in Process</li>
      <li>Smart Search</li>
      <li>Organise and link your personal data</li>
      <li>Left &amp; Right hand Smart Interface</li>
      <li>Buying Power</li>
    </ul>
  </section>

  <section class="needs-bubble">
    <ul class="bullet-list">
      <li>Establish your needs, wants &amp; wishes</li>
      <li>Make your money go further</li>
      <li>User ranked product suppliers</li>
      <li>Providing the tools you need</li>
      <li>Smart Recommendations specified by you</li>
    </ul>
  </section>

  <div class="figure figure--orange" role="img" aria-label="Flat orange figure of a person holding the product sign"></div>
  <div class="figure figure--green" role="img" aria-label="Flat green figure of a second person standing beside the sign"></div>
  <h1 class="product-name"><span>Sky</span><span>Nest</span></h1>

  <div class="sharing">
    <div class="sharing__art" role="img" aria-label="Circle of colourful people holding hands, representing the sharing economy"></div>
    <p class="sharing__label">Sharing Economy</p>
  </div>

  <footer class="footer">
    <p>T: +44 (0) 20 7946 0132</p>
    <p>www.brightlanesystems.com</p>
  </footer>
</main>
</body>
</html>
```